Vantrisco website redesign

1.logo redesign
2. whole website lay out redesign
3. add more function and pages (have some detail in attachment).
4. design the info taking form layout(contact us, return request, trade pro, see all form in file)
5. also design the mobile look for the website
some reference website: https://www.plaquevora.example/
https://www.moskuden.example/

we want our website style between these two website, website should be user friendly focus + slight design style, and mobile one could more like https://www.moskuden.example/ (more design style)

Target Market(s)

Tile Ecommerce

Industry/Entity Type

Ecommerce, Tile

Coding

Coded - Design and coding required

Number of Pages Required

5+ page

```html
<!DOCTYPE html>
<html lang="en">
<head>
<meta charset="utf-8">
<title>Vantrisco – Home page, default and contact states</title>
<link rel="stylesheet" href="https://fonts.googleapis.com/css2?family=Caveat+Brush&family=Poppins:wght@400;500;600;700&display=swap">
<style>
:root{
  --ink:#2b2b2b;
  --nav:#6f6f6f;
  --grey-btn:#6b6b6b;
  --soft:#e4e3e4;
  --white:#ffffff;
  --text:#4a4a4a;
  --muted:#8a8a8a;
  --stage:#ffffff;
}
*{box-sizing:border-box;margin:0;padding:0}
html,body{width:711px;height:1200px;overflow:hidden;background:var(--stage)}
body{position:relative;font-family:"Poppins",sans-serif;color:var(--text)}
.page{position:absolute;top:15px;width:650px;height:2440px;transform:scale(.479);transform-origin:0 0;overflow:hidden;background:var(--white);box-shadow:0 0 12px rgba(0,0,0,.15)}
.page--default{left:31px}
.page--contact{left:369px}
.section-title{font-family:"Caveat Brush",cursive;font-size:22px;color:var(--ink);text-align:center;letter-spacing:.5px;text-transform:uppercase}

.promo-bar{height:28px;background:var(--ink);color:var(--white);font-size:7px;display:flex;align-items:center;justify-content:center;gap:22px}
.promo-bar .arrow{width:8px;height:8px;border-radius:50%;background:var(--white);color:var(--ink);font-size:6px;line-height:8px;text-align:center}
.header{height:40px;position:relative}
.logo{position:absolute;left:60px;top:9px;font-family:"Poppins",sans-serif;font-weight:600;font-size:18px;color:var(--ink)}
.search{position:absolute;left:210px;top:9px;width:215px;height:22px;border:1px solid #ddd;font-size:6px;color:#444;padding-left:6px;line-height:20px}
.search .go{position:absolute;right:-1px;top:-1px;width:28px;height:22px;background:var(--ink)}
.search .go svg{position:absolute;left:9px;top:6px}
.btn{position:absolute;top:9px;height:22px;font-size:8px;font-weight:600;color:var(--white);text-align:center;line-height:22px;letter-spacing:.4px}
.btn--trade{left:440px;width:65px;background:var(--ink)}
.btn--about{left:518px;width:71px;background:var(--grey-btn)}
.nav{height:33px;background:var(--nav);display:flex;align-items:center;padding-left:60px;gap:22px;font-size:8px;color:var(--white);position:relative}
.nav .caret{font-size:6px;margin-left:5px}
.nav-icons{position:absolute;right:60px;top:8px;display:flex;gap:6px}
.nav-icons span{width:17px;height:17px;border-radius:50%;background:var(--white)}

.hero{height:337px;position:relative;background:linear-gradient(100deg,#4d4d52 0%,#6b6660 30%,#8c5a3a 48%,#c29a64 62%,#7c7a80 80%,#55575e 100%)}
.hero::after{content:"";position:absolute;inset:0;background:linear-gradient(90deg,rgba(30,30,30,.55),rgba(30,30,30,0) 60%)}
.hero-copy{position:absolute;left:60px;top:90px;z-index:1;color:var(--white)}
.hero-kicker{font-family:"Caveat Brush",cursive;font-size:18px}
.hero-title{font-family:"Caveat Brush",cursive;font-size:32px;line-height:1;letter-spacing:1px}
.hero-text{font-size:8px;line-height:17px;width:260px;margin-top:10px}
.hero-btn{display:block;margin-top:12px;width:80px;height:22px;background:var(--white);color:var(--ink);font-size:8px;font-weight:600;text-align:center;line-height:22px}
.dots{display:flex;gap:6px;justify-content:center}
.dots span{width:6px;height:6px;background:#bbb}
.dots span.on{background:var(--ink)}
.hero .dots{position:absolute;left:0;right:0;bottom:20px;z-index:1}
.hero .dots span{background:#ddd}
.hero .dots span.on{background:var(--white)}

.journey{height:254px;padding-top:32px}
.tile-cards{display:flex;gap:31px;margin:24px 0 0 60px}
.tile-card{width:156px;height:138px;position:relative;border-radius:3px;overflow:hidden}
.tile-card .label{position:absolute;left:0;right:0;bottom:8px;text-align:center;color:var(--white);font-size:8px;font-weight:700;letter-spacing:.3px}
.tile-card::after{content:"";position:absolute;inset:0;background:linear-gradient(180deg,rgba(0,0,0,0) 60%,rgba(0,0,0,.6))}
.tile-card .label{z-index:1}

.explore{height:339px;background:var(--soft);padding-top:32px}
.collection-cards{display:flex;gap:31px;margin:24px 0 0 60px}
.collection-card{width:156px;height:224px;background:var(--white);border-radius:3px;overflow:hidden}
.collection-card .photo{height:110px}
.collection-card .body{padding:12px 13px}
.collection-card h3{font-size:8px;font-weight:600;color:var(--ink);letter-spacing:.3px}
.collection-card p{font-size:6.8px;line-height:14px;margin-top:4px;color:var(--text)}
.collection-card .more{font-size:7px;font-weight:500;color:var(--ink);margin-top:10px}

.colors{height:259px;padding-top:33px}
.palettes{position:relative;height:140px;margin-top:20px}
.palette{position:absolute;background:var(--white);box-shadow:0 2px 8px rgba(0,0,0,.12);display:flex;flex-direction:column;justify-content:space-between}
.palette .row{flex:none;background:repeating-linear-gradient(90deg,var(--c) 0 var(--w),transparent var(--w) var(--s))}
.palette--s1{left:40px;top:20px;width:83px;height:88px;padding:5px}
.palette--s2{left:140px;top:10px;width:100px;height:107px;padding:6px}
.palette--main{left:265px;top:0;width:120px;height:127px;padding:6px;box-shadow:0 4px 14px rgba(0,0,0,.25)}
.palette--s4{left:405px;top:10px;width:100px;height:107px;padding:6px}
.palette--s5{left:525px;top:20px;width:83px;height:88px;padding:5px}
.palette--s1 .row,.palette--s5 .row{height:10px;--w:13px;--s:15px}
.palette--s2 .row,.palette--s4 .row{height:13px;--w:15px;--s:18px}
.palette--main .row{height:16px;--w:19px;--s:22px}
.palette--s1,.palette--s5{opacity:.75}
.colors .dots{margin-top:2px}

.inspiration{height:331px;background:var(--soft);padding-top:32px}
.insta-row{display:flex;justify-content:space-between;margin-top:24px}
.insta{width:144px;height:168px;position:relative}
.insta::after{content:"";position:absolute;inset:0;background:linear-gradient(180deg,rgba(0,0,0,0) 65%,rgba(0,0,0,.6))}
.insta .label{position:absolute;left:0;right:0;bottom:8px;text-align:center;color:var(--white);font-size:7.5px;font-weight:700;z-index:1}
.view-all{display:block;width:80px;height:22px;margin:34px auto 0;background:var(--ink);color:var(--white);font-size:7.5px;font-weight:600;text-align:center;line-height:22px}

.projects{height:291px;padding-top:33px;position:relative}
.project{position:absolute}
.project--left{left:14px;top:92px;width:182px;height:117px}
.project--center{left:211px;top:77px;width:228px;height:147px;box-shadow:0 2px 8px rgba(0,0,0,.15)}
.project--right{left:453px;top:92px;width:182px;height:117px}
.projects .dots{position:absolute;left:0;right:0;top:246px}

.reviews{height:301px;background:var(--soft);padding-top:33px}
.review-cards{display:flex;gap:15px;margin:36px 0 0 74px}
.review{width:166px;height:170px;background:var(--white);border-radius:3px;position:relative;padding:26px 12px 0}
.review .quote{position:absolute;left:12px;top:-12px;width:24px;height:24px;background:#4d4d4d;color:var(--white);font-family:Georgia,serif;font-size:22px;line-height:30px;text-align:center}
.review p{font-size:7.2px;line-height:16.5px;color:var(--text)}
.review .who{border-top:1px solid #777;margin-top:10px;padding-top:8px}
.review .name{font-size:10px;font-weight:600;color:#333}
.review .place{font-size:6px;font-weight:600;color:#333}

.footer{height:227px;background:var(--ink);color:var(--white);position:relative}
.footer .logo{color:var(--white);top:30px;font-size:18px}
.foot-col{position:absolute;top:80px}
.foot-col h4{font-family:"Caveat Brush",cursive;font-weight:400;font-size:15px;letter-spacing:.5px;margin-bottom:8px}
.foot-col li{list-style:none;font-size:7.5px;line-height:16.5px}
.foot-col--contact{left:60px}
.foot-col--contact li{display:flex;align-items:center;gap:14px;line-height:30px}
.foot-col--experience{left:236px}
.foot-col--about{left:417px}
.foot-col--about h4.follow{margin-top:14px}
.foot-col--about .social{display:flex;align-items:center;gap:14px}
.social .sq{width:9px;height:9px;border:1.5px solid var(--white);border-radius:2px}
.chat{position:absolute;left:568px;top:164px}
.foot-rule{position:absolute;left:60px;right:60px;top:196px;border-top:1px solid #555}
.copyright{position:absolute;left:0;right:0;top:207px;text-align:center;font-size:7.5px}

.dim{position:absolute;inset:0 0 227px 0;background:rgba(60,60,60,.42)}
.dim--foot{position:absolute;left:0;right:0;bottom:0;height:227px;background:rgba(60,60,60,.1)}
.contact-form{position:absolute;left:456px;top:2238px;width:132px;height:116px;background:var(--white);border-radius:3px;padding:8px 10px;font-size:4px;color:#555;z-index:2}
.contact-form .grid{display:grid;grid-template-columns:1fr 1fr;gap:5px 8px}
.contact-form .field{height:10px;border:.8px solid #bbb;margin-top:2px}
.contact-form .send{width:50px;height:10px;background:var(--ink);color:var(--white);font-size:5px;text-align:center;line-height:10px;margin-top:7px}
.contact-form .note{margin-top:5px;font-size:5px;font-weight:600;color:#333}
.contact-form .note span{display:block;font-weight:400;font-size:4px;line-height:5.5px;color:#666;margin-top:1px}
</style>
</head>
<body>

<!-- Default state -->
<div class="page page--default">
  <div class="promo-bar"><span class="arrow">‹</span><span>Wholesale, over 150 square feet. 10% off</span><span class="arrow">›</span></div>
  <div class="header">
    <div class="logo">Vantrisco</div>
    <div class="search">Search For Your Favorite Tiles<span class="go"><svg width="10" height="10" viewBox="0 0 10 10"><circle cx="4" cy="4" r="3" fill="none" stroke="#fff" stroke-width="1.2"/><path d="M6.3 6.3 9 9" stroke="#fff" stroke-width="1.2"/></svg></span></div>
    <div class="btn btn--trade">TRADE</div>
    <div class="btn btn--about">ABOUT US</div>
  </div>
  <div class="nav"><span>Home</span><span>New</span><span>Porcelain Tile<span class="caret">▼</span></span><span>Ceramic Tile<span class="caret">▼</span></span><span>Glass Tile<span class="caret">▼</span></span><span>Marble Fixture</span><div class="nav-icons"><span></span><span></span></div></div>
  <div class="hero" role="img" aria-label="Photo of stone and marble tile slabs on display racks">
    <div class="hero-copy"><div class="hero-kicker">WELCOME TO</div><div class="hero-title">VANTRISCO</div><p class="hero-text">Lorem ipsum dolor sit amet, consectetur adipiscing elit, sed do eiusmod tempor incididunt ut labore et dolore magna aliqua.</p><span class="hero-btn">SHOP NOW</span></div>
    <div class="dots"><span></span><span></span><span class="on"></span><span></span><span></span></div>
  </div>
  <section class="journey">
    <h2 class="section-title">New Journey Starts</h2>
    <div class="tile-cards">
      <div class="tile-card" role="img" aria-label="Checkerboard of wood and stone mosaic tiles" style="background:linear-gradient(135deg,#8a5a2e,#d9d2c6 45%,#9a6a3a 70%,#e0dbd2)"><span class="label">BEST SELLERS ➜</span></div>
      <div class="tile-card" role="img" aria-label="Couple browsing tile samples in a showroom" style="background:linear-gradient(120deg,#8fa2b8,#d9dde2 45%,#a7b0bd 75%,#6e7a88)"><span class="label">NEW ARRIVALS ➜</span></div>
      <div class="tile-card" role="img" aria-label="Assorted stone and wood-look tiles" style="background:linear-gradient(135deg,#b49a80,#7d5f48 40%,#c8b39c 70%,#6a4c38)"><span class="label">ALL COLLECTIONS ➜</span></div>
    </div>
  </section>
  <section class="explore">
    <h2 class="section-title">Explore the Collection</h2>
    <div class="collection-cards">
      <div class="collection-card"><div class="photo" role="img" aria-label="Bright bathroom with checkered floor" style="background:linear-gradient(180deg,#ecebe8,#d8cfc2 60%,#3a3a3a)"></div><div class="body"><h3>GLASS COLLECTION</h3><p>Known For Its Striking Sheen And Vivid, Long-Lasting Colors, Our Glass Tile Brings A Luxurious Dimension To Modern.</p><div class="more">SHOP NOW ➜</div></div></div>
      <div class="collection-card"><div class="photo" role="img" aria-label="White kitchen with navy cabinets" style="background:linear-gradient(180deg,#f1f1f0,#dcdcdc 45%,#2d3e5c)"></div><div class="body"><h3>CERAMIC COLLECTION</h3><p>Crafted For Both Strength And Elegance, Our Ceramic Tile Transforms Any Space With Its Rich Textures And Array Of Hues.</p><div class="more">SHOP NOW ➜</div></div></div>
      <div class="collection-card"><div class="photo" role="img" aria-label="Warm kitchen with stone island and garden view" style="background:linear-gradient(180deg,#6b4a34,#4e5a3a 45%,#a89a88)"></div><div class="body"><h3>PORCELAIN COLLECTION</h3><p>Renowned For Its Robustness And Refined Finish, Our Porcelain Tile Is Perfect For Both Indoor And Outdoor Settings.</p><div class="more">SHOP NOW ➜</div></div></div>
    </div>
  </section>
  <section class="colors">
    <h2 class="section-title">Find Your Color</h2>
    <div class="palettes">
      <div class="palette palette--s1"><div class="row" style="--c:#fde3a7"></div><div class="row" style="--c:#fcdca0"></div><div class="row" style="--c:#fbd39b"></div><div class="row" style="--c:#f9cba0"></div><div class="row" style="--c:#f6c3a3"></div><div class="row" style="--c:#f3bca4"></div></div>
      <div class="palette palette--s2"><div class="row" style="--c:#b9e4cb"></div><div class="row" style="--c:#acdcb5"></div><div class="row" style="--c:#b8dca0"></div><div class="row" style="--c:#c6e095"></div><div class="row" style="--c:#d3e48d"></div><div class="row" style="--c:#dde785"></div></div>
      <div class="palette palette--main"><div class="row" style="--c:#2db3e6"></div><div class="row" style="--c:#1a9bd0"></div><div class="row" style="--c:#137aa6"></div><div class="row" style="--c:#0f5d80"></div><div class="row" style="--c:#0c445c"></div><div class="row" style="--c:#0a2f3e"></div></div>
      <div class="palette palette--s4"><div class="row" style="--c:#f08a8f"></div><div class="row" style="--c:#e98d94"></div><div class="row" style="--c:#d48a93"></div><div class="row" style="--c:#b98089"></div><div class="row" style="--c:#a07a80"></div><div class="row" style="--c:#8b7479"></div></div>
      <div class="palette palette--s5"><div class="row" style="--c:#a9c6e6"></div><div class="row" style="--c:#b3d2ee"></div><div class="row" style="--c:#a8dce9"></div><div class="row" style="--c:#b2e3e4"></div><div class="row" style="--c:#c0e7df"></div><div class="row" style="--c:#cdeadb"></div></div>
    </div>
    <div class="dots"><span></span><span></span><span class="on"></span><span></span><span></span></div>
  </section>
  <section class="inspiration">
    <h2 class="section-title">Inspiration</h2>
    <div class="insta-row">
      <div class="insta" role="img" aria-label="Airy living room with sofa and olive tree" style="background:linear-gradient(180deg,#e8e4dc,#cfc8bb 60%,#6b665e)"><span class="label">@ROOMSBYLENA ➜</span></div>
      <div class="insta" role="img" aria-label="Kitchen with green cabinets and copper hood" style="background:linear-gradient(180deg,#b0683a,#4f5e3b 45%,#3c4a2e)"><span class="label">@STUDIOHARVEL ➜</span></div>
      <div class="insta" role="img" aria-label="Bathroom with floral wallpaper and freestanding tub" style="background:linear-gradient(180deg,#d9c4b8,#5e8a6a 40%,#ece8e2)"><span class="label">@ATELIERMORRA.DESIGN ➜</span></div>
      <div class="insta" role="img" aria-label="White kitchen with brass pendant lights" style="background:linear-gradient(180deg,#f0eee9,#d6cfc0 50%,#8c7a60)"><span class="label">@KORVENDESIGN ➜</span></div>
    </div>
    <span class="view-all">VIEW ALL</span>
  </section>
  <section class="projects">
    <h2 class="section-title">Complete Your Projects</h2>
    <div class="project project--left" role="img" aria-label="Shower with dark wood-look wall tile" style="background:linear-gradient(90deg,#2e2e2e,#575757 55%,#6b6b6b)"></div>
    <div class="project project--center" role="img" aria-label="White bathroom with double vanity and tub" style="background:linear-gradient(180deg,#f2f2f2,#dcdcdc 55%,#9a7a5a)"></div>
    <div class="project project--right" role="img" aria-label="Minimal bathroom with freestanding tub" style="background:linear-gradient(90deg,#d9d9d9,#c4c4c4 60%,#a99a86)"></div>
    <div class="dots"><span></span><span></span><span class="on"></span><span></span><span></span></div>
  </section>
  <section class="reviews">
    <h2 class="section-title">What Our Customers Are Saying</h2>
    <div class="review-cards">
      <div class="review"><span class="quote">“</span><p>Outstanding service, great choices. Staff helped us with four distinct full floor home projects, and in every instance have been responsive and resourceful.</p><div class="who"><div class="name">Tomas L</div><div class="place">SPRINGFIELD, MA</div></div></div>
      <div class="review"><span class="quote">“</span><p>They have everything you need to do a tile job and employees are quite helpful and knowledgeable about their products and the things you'll need.</p><div class="who"><div class="name">Marcel D</div><div class="place">POUGHKEEPSIE, NY</div></div></div>
      <div class="review"><span class="quote">“</span><p>This place is the best. I was there shortly before closing but they were very patient and explained every detail to me. Gave me great advice.</p><div class="who"><div class="name">Leon V</div><div class="place">FREDERICK, MD</div></div></div>
    </div>
  </section>
  <footer class="footer">
    <div class="logo">Vantrisco</div>
    <div class="foot-col foot-col--contact"><h4>CONTACT US</h4><ul><li><svg width="9" height="9" viewBox="0 0 10 10"><path d="M2 1l2 2-1 1.5c.6 1.2 1.3 1.9 2.5 2.5L7 6l2 2-1.5 1.5C4.5 9 1 5.5.5 2.5z" fill="#fff"/></svg>555-014-2277</li><li><svg width="10" height="8" viewBox="0 0 10 8"><rect x=".5" y=".5" width="9" height="7" fill="none" stroke="#fff"/><path d="M.5.5 5 4.5 9.5.5" fill="none" stroke="#fff"/></svg>hello@vantrisco.example</li></ul></div>
    <div class="foot-col foot-col--experience"><h4>CLIENT EXPERIENCE</h4><ul><li>Shipping &amp; Returns</li><li>FAQs</li><li>My Account</li><li>Track My Order</li><li>Installation</li></ul></div>
    <div class="foot-col foot-col--about"><h4>ABOUT US</h4><ul><li>Inspiration</li><li>Trade</li></ul><h4 class="follow">FOLLOW US</h4><div class="social"><span class="sq"></span><span style="font-size:7.5px">photofeed</span></div></div>
    <svg class="chat" width="22" height="20" viewBox="0 0 22 20"><rect x="1" y="6" width="13" height="9" rx="2" fill="none" stroke="#fff"/><path d="M7 6V3a2 2 0 0 1 2-2h8a2 2 0 0 1 2 2v6a2 2 0 0 1-2 2h-3" fill="none" stroke="#fff"/><circle cx="19" cy="2" r="2" fill="#4cd137"/></svg>
    <div class="foot-rule"></div>
    <div class="copyright">© 2024 Vantrisco. All Rights Reserved</div>
  </footer>
</div>

<!-- Contact form state -->
<div class="page page--contact">
  <div class="promo-bar"><span class="arrow">‹</span><span>Wholesale, over 150 square feet. 10% off</span><span class="arrow">›</span></div>
  <div class="header">
    <div class="logo">Vantrisco</div>
    <div class="search">Search For Your Favorite Tiles<span class="go"><svg width="10" height="10" viewBox="0 0 10 10"><circle cx="4" cy="4" r="3" fill="none" stroke="#fff" stroke-width="1.2"/><path d="M6.3 6.3 9 9" stroke="#fff" stroke-width="1.2"/></svg></span></div>
    <div class="btn btn--trade">TRADE</div>
    <div class="btn btn--about">ABOUT US</div>
  </div>
  <div class="nav"><span>Home</span><span>New</span><span>Porcelain Tile<span class="caret">▼</span></span><span>Ceramic Tile<span class="caret">▼</span></span><span>Glass Tile<span class="caret">▼</span></span><span>Marble Fixture</span><div class="nav-icons"><span></span><span></span></div></div>
  <div class="hero" role="img" aria-label="Photo of stone and marble tile slabs on display racks">
    <div class="hero-copy"><div class="hero-kicker">WELCOME TO</div><div class="hero-title">VANTRISCO</div><p class="hero-text">Lorem ipsum dolor sit amet, consectetur adipiscing elit, sed do eiusmod tempor incididunt ut labore et dolore magna aliqua.</p><span class="hero-btn">SHOP NOW</span></div>
    <div class="dots"><span></span><span></span><span class="on"></span><span></span><span></span></div>
  </div>
  <section class="journey">
    <h2 class="section-title">New Journey Starts</h2>
    <div class="tile-cards">
      <div class="tile-card" role="img" aria-label="Checkerboard of wood and stone mosaic tiles" style="background:linear-gradient(135deg,#8a5a2e,#d9d2c6 45%,#9a6a3a 70%,#e0dbd2)"><span class="label">BEST SELLERS ➜</span></div>
      <div class="tile-card" role="img" aria-label="Couple browsing tile samples in a showroom" style="background:linear-gradient(120deg,#8fa2b8,#d9dde2 45%,#a7b0bd 75%,#6e7a88)"><span class="label">NEW ARRIVALS ➜</span></div>
      <div class="tile-card" role="img" aria-label="Assorted stone and wood-look tiles" style="background:linear-gradient(135deg,#b49a80,#7d5f48 40%,#c8b39c 70%,#6a4c38)"><span class="label">ALL COLLECTIONS ➜</span></div>
    </div>
  </section>
  <section class="explore">
    <h2 class="section-title">Explore the Collection</h2>
    <div class="collection-cards">
      <div class="collection-card"><div class="photo" role="img" aria-label="Bright bathroom with checkered floor" style="background:linear-gradient(180deg,#ecebe8,#d8cfc2 60%,#3a3a3a)"></div><div class="body"><h3>GLASS COLLECTION</h3><p>Known For Its Striking Sheen And Vivid, Long-Lasting Colors, Our Glass Tile Brings A Luxurious Dimension To Modern.</p><div class="more">SHOP NOW ➜</div></div></div>
      <div class="collection-card"><div class="photo" role="img" aria-label="White kitchen with navy cabinets" style="background:linear-gradient(180deg,#f1f1f0,#dcdcdc 45%,#2d3e5c)"></div><div class="body"><h3>CERAMIC COLLECTION</h3><p>Crafted For Both Strength And Elegance, Our Ceramic Tile Transforms Any Space With Its Rich Textures And Array Of Hues.</p><div class="more">SHOP NOW ➜</div></div></div>
      <div class="collection-card"><div class="photo" role="img" aria-label="Warm kitchen with stone island and garden view" style="background:linear-gradient(180deg,#6b4a34,#4e5a3a 45%,#a89a88)"></div><div class="body"><h3>PORCELAIN COLLECTION</h3><p>Renowned For Its Robustness And Refined Finish, Our Porcelain Tile Is Perfect For Both Indoor And Outdoor Settings.</p><div class="more">SHOP NOW ➜</div></div></div>
    </div>
  </section>
  <section class="colors">
    <h2 class="section-title">Find Your Color</h2>
    <div class="palettes">
      <div class="palette palette--s1"><div class="row" style="--c:#fde3a7"></div><div class="row" style="--c:#fcdca0"></div><div class="row" style="--c:#fbd39b"></div><div class="row" style="--c:#f9cba0"></div><div class="row" style="--c:#f6c3a3"></div><div class="row" style="--c:#f3bca4"></div></div>
      <div class="palette palette--s2"><div class="row" style="--c:#b9e4cb"></div><div class="row" style="--c:#acdcb5"></div><div class="row" style="--c:#b8dca0"></div><div class="row" style="--c:#c6e095"></div><div class="row" style="--c:#d3e48d"></div><div class="row" style="--c:#dde785"></div></div>
      <div class="palette palette--main"><div class="row" style="--c:#2db3e6"></div><div class="row" style="--c:#1a9bd0"></div><div class="row" style="--c:#137aa6"></div><div class="row" style="--c:#0f5d80"></div><div class="row" style="--c:#0c445c"></div><div class="row" style="--c:#0a2f3e"></div></div>
      <div class="palette palette--s4"><div class="row" style="--c:#f08a8f"></div><div class="row" style="--c:#e98d94"></div><div class="row" style="--c:#d48a93"></div><div class="row" style="--c:#b98089"></div><div class="row" style="--c:#a07a80"></div><div class="row" style="--c:#8b7479"></div></div>
      <div class="palette palette--s5"><div class="row" style="--c:#a9c6e6"></div><div class="row" style="--c:#b3d2ee"></div><div class="row" style="--c:#a8dce9"></div><div class="row" style="--c:#b2e3e4"></div><div class="row" style="--c:#c0e7df"></div><div class="row" style="--c:#cdeadb"></div></div>
    </div>
    <div class="dots"><span></span><span></span><span class="on"></span><span></span><span></span></div>
  </section>
  <section class="inspiration">
    <h2 class="section-title">Inspiration</h2>
    <div class="insta-row">
      <div class="insta" role="img" aria-label="Airy living room with sofa and olive tree" style="background:linear-gradient(180deg,#e8e4dc,#cfc8bb 60%,#6b665e)"><span class="label">@ROOMSBYLENA ➜</span></div>
      <div class="insta" role="img" aria-label="Kitchen with green cabinets and copper hood" style="background:linear-gradient(180deg,#b0683a,#4f5e3b 45%,#3c4a2e)"><span class="label">@STUDIOHARVEL ➜</span></div>
      <div class="insta" role="img" aria-label="Bathroom with floral wallpaper and freestanding tub" style="background:linear-gradient(180deg,#d9c4b8,#5e8a6a 40%,#ece8e2)"><span class="label">@ATELIERMORRA.DESIGN ➜</span></div>
      <div class="insta" role="img" aria-label="White kitchen with brass pendant lights" style="background:linear-gradient(180deg,#f0eee9,#d6cfc0 50%,#8c7a60)"><span class="label">@KORVENDESIGN ➜</span></div>
    </div>
    <span class="view-all">VIEW ALL</span>
  </section>
  <section class="projects">
    <h2 class="section-title">Complete Your Projects</h2>
    <div class="project project--left" role="img" aria-label="Shower with dark wood-look wall tile" style="background:linear-gradient(90deg,#2e2e2e,#575757 55%,#6b6b6b)"></div>
    <div class="project project--center" role="img" aria-label="White bathroom with double vanity and tub" style="background:linear-gradient(180deg,#f2f2f2,#dcdcdc 55%,#9a7a5a)"></div>
    <div class="project project--right" role="img" aria-label="Minimal bathroom with freestanding tub" style="background:linear-gradient(90deg,#d9d9d9,#c4c4c4 60%,#a99a86)"></div>
    <div class="dots"><span></span><span></span><span class="on"></span><span></span><span></span></div>
  </section>
  <section class="reviews">
    <h2 class="section-title">What Our Customers Are Saying</h2>
    <div class="review-cards">
      <div class="review"><span class="quote">“</span><p>Outstanding service, great choices. Staff helped us with four distinct full floor home projects, and in every instance have been responsive and resourceful.</p><div class="who"><div class="name">Tomas L</div><div class="place">SPRINGFIELD, MA</div></div></div>
      <div class="review"><span class="quote">“</span><p>They have everything you need to do a tile job and employees are quite helpful and knowledgeable about their products and the things you'll need.</p><div class="who"><div class="name">Marcel D</div><div class="place">POUGHKEEPSIE, NY</div></div></div>
      <div class="review"><span class="quote">“</span><p>This place is the best. I was there shortly before closing but they were very patient and explained every detail to me. Gave me great advice.</p><div class="who"><div class="name">Leon V</div><div class="place">FREDERICK, MD</div></div></div>
    </div>
  </section>
  <footer class="footer">
    <div class="logo">Vantrisco</div>
    <div class="foot-col foot-col--contact"><h4>CONTACT US</h4><ul><li><svg width="9" height="9" viewBox="0 0 10 10"><path d="M2 1l2 2-1 1.5c.6 1.2 1.3 1.9 2.5 2.5L7 6l2 2-1.5 1.5C4.5 9 1 5.5.5 2.5z" fill="#fff"/></svg>555-014-2277</li><li><svg width="10" height="8" viewBox="0 0 10 8"><rect x=".5" y=".5" width="9" height="7" fill="none" stroke="#fff"/><path d="M.5.5 5 4.5 9.5.5" fill="none" stroke="#fff"/></svg>hello@vantrisco.example</li></ul></div>
    <div class="foot-col foot-col--experience" style="left:212px"><h4>CLIENT EXPERIENCE</h4><ul><li>Shipping &amp; Returns</li><li>FAQs</li><li>My Account</li><li>Track My Order</li><li>Installation</li></ul></div>
    <div class="foot-col foot-col--about" style="left:370px"><h4>ABOUT US</h4><ul><li>Inspiration</li><li>Trade</li></ul><h4 class="follow">FOLLOW US</h4><div class="social"><span class="sq"></span><span style="font-size:7.5px">photofeed</span></div></div>
    <svg class="chat" width="22" height="20" viewBox="0 0 22 20"><rect x="1" y="6" width="13" height="9" rx="2" fill="none" stroke="#fff"/><path d="M7 6V3a2 2 0 0 1 2-2h8a2 2 0 0 1 2 2v6a2 2 0 0 1-2 2h-3" fill="none" stroke="#fff"/><circle cx="19" cy="2" r="2" fill="#4cd137"/></svg>
    <div class="foot-rule"></div>
    <div class="copyright">© 2024 Vantrisco. All Rights Reserved</div>
  </footer>
  <div class="dim"></div>
  <form class="contact-form">
    <div class="grid">
      <label>Name<div class="field"></div></label>
      <label>Phone<div class="field"></div></label>
      <label>E-mail<div class="field"></div></label>
      <label>Message<div class="field"></div></label>
    </div>
    <div class="send">SEND</div>
    <div class="note">Disclaimer :<span>We reply within one business day, thank you for reaching out to us.</span></div>
  </form>
</div>

</body>
</html>
```